Tolvene Hub Redesign

tolvenehub.com is one of our old, high-traffic multilingual site.

its interface is very old, so we want to redesign it to give a modern, attractive design, with comfortable colors and layout.

beside the current content of the main page we want to add two places for dynamic banners.

The site has an App in iOS and Android, we want an ad in a noticeable place for it.

this ad will be permanent.

the site now has 12 languages, but we may add new languages soon, so design must consider this.

redesign of two internal pages also required:
- the main listing page, example: http://www.tolvenehub.example/en/cat/252
- the article view page: http://www.tolvenehub.example/en/10323

Reason: want to receive more designs ...

```html
<!DOCTYPE html>
<html lang="en">
<head>
<meta charset="utf-8">
<title>Tolvene Hub – Questions &amp; Answers</title>
<link href="https://fonts.googleapis.com/css2?family=Arimo:wght@400;700&family=Caladea:wght@400;700&family=Oswald:wght@400;500&display=swap" rel="stylesheet">
<style>
:root{
  --sky-top:#4f9fe0;
  --sky-mid:#8ccbf2;
  --sky-light:#d9effb;
  --nav-dark:#0f6fae;
  --cyan:#35c0de;
  --cyan-dark:#1ea9c9;
  --footer-cyan:#4ec8e1;
  --footer-bar:#177d8f;
  --heading-blue:#2b6fb8;
  --text:#333a40;
  --line:#d9dde0;
  --row:#eeeeee;
  --green:#5cb531;
  --green-dark:#3f9a1f;
  --ad-blue:#0c3f7a;
  --ad-light:#a9d3f2;
  --orange:#f7931e;
  --navy:#1b3e6e;
  --page:#ffffff;
}
*{box-sizing:border-box;margin:0;padding:0}
html,body{width:785px;height:1200px;overflow:hidden;background:var(--page)}
body{position:relative;font-family:"Arimo",Arial,sans-serif;color:var(--text);font-size:10px}
.abs{position:absolute}
a{color:inherit;text-decoration:none}

/* header */
.header{left:0;top:0;width:785px;height:202px;background:linear-gradient(160deg,var(--sky-top) 0%,var(--sky-mid) 45%,var(--sky-light) 75%,var(--sky-mid) 100%)}
.brand{left:106px;top:14px;font-family:"Oswald",sans-serif;font-size:30px;font-weight:500;color:#f2d21a;display:flex;align-items:center;gap:8px}
.brand-mark{width:14px;height:14px;border-radius:50%;background:#f2d21a}
.brand-sub{left:106px;top:54px;font-size:8px;color:#2a6fb0;letter-spacing:.5px}
.main-nav{left:370px;top:20px;width:310px;height:22px;background:linear-gradient(#3aa2e2,var(--nav-dark));border-radius:3px;display:flex;font-size:8px;color:#fff;border:1px solid #7cc3ee}
.main-nav a{flex:1;display:flex;align-items:center;justify-content:center}
.main-nav a.active{background:var(--nav-dark);box-shadow:inset 0 0 0 1px #0a5a90}
.hero-title{left:106px;top:74px;font-family:"Caladea",serif;font-size:20px;font-weight:400;line-height:24px;color:#3a3f63}
.hero-title span{color:#9a5a1a}
.hero-text{left:106px;top:125px;width:250px;font-size:8.5px;line-height:12px;font-weight:700;color:#3d4a70}
.hero-art{left:444px;top:72px;width:192px;height:128px;border-radius:6px;background:radial-gradient(ellipse at 50% 45%,#ffffff 0%,#e6eef2 40%,rgba(140,100,70,.5) 75%,rgba(140,200,240,0) 100%)}
.search-tab{left:108px;top:170px;width:252px;height:30px;background:linear-gradient(var(--green),var(--green-dark));border-radius:20px 20px 0 0;display:flex;align-items:center;padding-left:32px;gap:6px}
.search-field{width:120px;height:17px;background:#fff;border:1px solid #b9d9a8;font-size:8.5px;color:#aaa;padding:3px 5px}
.search-btn{width:90px;height:17px;background:linear-gradient(#7dcf4f,#4aa525);border:1px solid #e5f5da;color:#fff;font-size:10px;display:flex;align-items:center;justify-content:center;gap:4px}

/* languages */
.lang-bar{left:0;top:202px;width:785px;height:33px;background:linear-gradient(var(--cyan),var(--cyan-dark));border-top:1px solid #a5e3f1}
.lang-list{left:100px;top:202px;height:33px;display:flex;font-size:9px;font-weight:700;color:#fff}
.lang-list li{list-style:none;display:flex;flex-direction:column;align-items:center;justify-content:center;padding:0 10px}
.lang-list li.active{background:#fff;color:var(--text);font-weight:400}
.lang-list small{font-size:6px;font-weight:400;line-height:7px}

/* panels */
.panel{background:#fff;border:1px solid var(--line)}
.fatwas{left:100px;top:244px;width:426px;height:368px}
.section-title{font-family:"Oswald",sans-serif;font-size:14px;font-weight:500;color:var(--heading-blue)}
.fatwas .section-title{left:6px;top:7px}
.fatwas .rule{left:90px;top:17px;width:280px;height:1px;background:var(--line)}
.pager{left:374px;top:10px;display:flex;gap:2px}
.pager span{width:14px;height:14px;background:var(--cyan);color:#fff;font-size:8px;display:flex;align-items:center;justify-content:center}
.fatwa-list{left:6px;top:36px;width:413px;list-style:none}
.fatwa-list li{height:22.6px;display:flex;align-items:center;gap:8px;padding-left:5px;font-size:9px}
.fatwa-list li:nth-child(odd){background:var(--row)}
.fatwa-list li.tall{height:30px;line-height:11px}
.bullet{flex:none;width:11px;height:11px;border-radius:50%;background:var(--green);display:flex;align-items:center;justify-content:center}

.side{left:533px;width:147px}
.cats{top:244px;height:182px}
.files{top:431px;height:181px}
.side .section-title{position:absolute;left:8px;top:8px;font-size:12px}
.side .rule{position:absolute;left:8px;top:27px;width:130px;height:1px;background:var(--line)}
.side-list{position:absolute;left:8px;top:32px;width:132px;list-style:none}
.side-list li{display:flex;gap:6px;align-items:flex-start;font-size:7.5px;color:#555;padding:6px 0 5px;border-bottom:1px solid #eee;line-height:9px}
.tick{flex:none;width:8px;height:8px;border:1px solid var(--green);display:flex;align-items:center;justify-content:center}
.full-list{position:absolute;right:10px;bottom:8px;border:1px solid #b7dba2;color:var(--green);font-size:7.5px;font-weight:700;padding:2px 4px 2px 6px;display:flex;gap:6px;background:#fff}

/* topics */
.topics{left:100px;top:618px;width:426px;height:264px}
.topic{width:142px;height:110px;display:flex;flex-direction:column;align-items:center;text-align:center}
.topic-icon{width:40px;height:36px;border-radius:8px;margin:12px 0 10px}
.topic h3{font-family:"Oswald",sans-serif;font-weight:400;font-size:10px;color:var(--heading-blue);margin-bottom:6px}
.topic h3 em{font-style:normal;color:var(--green)}
.topic p{font-size:8.5px;line-height:10px;color:#555}
.vline{width:1px;background:#e3e3e3}
.hline{left:120px;top:126px;width:286px;height:1px;background:#e3e3e3}

/* cash ad */
.cash-ad{left:533px;top:618px;width:147px;height:368px;padding:4px}
.cash-inner{position:relative;width:100%;height:100%;background:linear-gradient(var(--ad-light),#dceefa 25%,#cfe6f7)}
.apply{position:absolute;left:20px;width:100px;height:24px;border-radius:12px;background:linear-gradient(#ffad3c,var(--orange));border:2px solid #fff;color:#fff;font-weight:700;font-size:12px;display:flex;align-items:center;justify-content:center;box-shadow:0 1px 2px rgba(0,0,0,.3)}
.cash-head{position:absolute;left:0;width:100%;text-align:center;color:var(--navy);font-weight:700;font-size:25px;line-height:26px}
.cash-mid{position:absolute;left:0;top:118px;width:100%;height:112px;background:linear-gradient(#2462a8,var(--ad-blue));color:#fff;padding:16px 0 0 16px;font-size:8.5px}
.cash-mid li{list-style:none;display:flex;gap:5px;align-items:center;margin-bottom:3px}
.check{width:9px;height:9px;border-radius:50%;background:#b9d5ee}
.cash-mid strong{display:block;text-align:center;margin-left:-16px;margin-top:14px;font-size:9px;font-weight:400}
.cash-mid strong b{display:block;font-size:11px;font-weight:700}

/* finance banner */
.finance{left:100px;top:889px;width:426px;height:97px;padding:6px}
.finance-inner{display:flex;height:100%}
.finance-text{width:255px;flex:none;background:#4a77b4;color:#fff;font-size:16px;letter-spacing:-.2px;display:flex;align-items:center;padding-left:8px;white-space:nowrap;overflow:hidden}
.finance-photo{flex:1;background:linear-gradient(#cfe3f6,#a7c3de 55%,#6b7d8c)}

/* footer */
.footer{left:0;top:994px;width:785px;height:168px;background:var(--footer-cyan)}
.about-title{left:106px;top:1015px;font-family:"Oswald",sans-serif;font-size:14px;font-weight:400;color:var(--navy)}
.about-title span{color:#fff}
.about-text{left:106px;top:1042px;width:232px;font-size:7px;line-height:9px;color:var(--navy)}
.social{left:110px;top:1120px;display:flex;gap:6px}
.social span{width:22px;height:22px;border-radius:50%}
.foot-col{top:1024px}
.foot-col h4{font-family:"Oswald",sans-serif;font-weight:400;font-size:9.5px;color:var(--navy);border-bottom:1px solid #8adcec;padding-bottom:3px;width:84px;margin-bottom:5px}
.foot-col li{list-style:none;font-size:7.5px;line-height:12px;color:var(--navy)}
.store{width:98px;height:32px;background:#111;border-radius:4px;border:1px solid #777;margin-bottom:7px}
.copyright{left:0;top:1162px;width:785px;height:38px;background:var(--footer-bar);color:#fff;font-size:7.5px;padding:10px 0 0 500px}
</style>
</head>
<body>

<header class="abs header"></header>
<div class="abs brand"><span class="brand-mark"></span>Tolvene Hub</div>
<div class="abs brand-sub">QUESTIONS &amp; ANSWERS</div>
<nav class="abs main-nav">
  <a class="active" href="#">HOME</a><a href="#">SHOWCASE</a><a href="#">ROOMS</a><a href="#">ABOUT</a><a href="#">GALLERY</a><a href="#">CONTACT</a>
</nav>
<h1 class="abs hero-title">Are You Looking For Islamic<br><span>Questions Answers?</span></h1>
<p class="abs hero-text">Parturient monte scetur ravida necluctus rem. Maecenas tristiqurci ferode.parturnt monte scetur ravida necluctus rem. Maecenas tristiqurci ferode.</p>
<div class="abs hero-art" role="img" aria-label="Open book resting on a wooden stand"></div>
<div class="abs search-tab">
  <div class="search-field">SEARCH KEYWORDS</div>
  <div class="search-btn"><svg width="9" height="9" viewBox="0 0 10 10"><circle cx="4" cy="4" r="3" fill="none" stroke="#fff" stroke-width="1.5"/><line x1="6.3" y1="6.3" x2="9" y2="9" stroke="#fff" stroke-width="1.5"/></svg>Search</div>
</div>

<div class="abs lang-bar"></div>
<ul class="abs lang-list">
  <li class="active">English</li><li>中文</li><li>Uygur</li><li>Français</li><li>Español</li><li style="padding:0 16px">日本語</li><li>Indonesian</li><li>Русский<small>New</small></li><li>Turk</li><li>Urdu</li><li style="padding:0 24px">Hindi<small>New</small></li>
</ul>

<section class="abs panel fatwas">
  <h2 class="abs section-title">NEW FATWAS</h2>
  <div class="abs rule"></div>
  <div class="abs pager"><span>‹</span><span>≡</span><span>›</span></div>
  <ul class="abs fatwa-list">
    <li><span class="bullet"><svg width="7" height="5"><path d="M1 1l2.5 3L6 1" fill="none" stroke="#fff" stroke-width="1.3"/></svg></span>His mother mistreats his wife and her family.</li>
    <li><span class="bullet"><svg width="7" height="5"><path d="M1 1l2.5 3L6 1" fill="none" stroke="#fff" stroke-width="1.3"/></svg></span>Partner took money from the company without his partner’s knowledge.</li>
    <li class="tall"><span class="bullet"><svg width="7" height="5"><path d="M1 1l2.5 3L6 1" fill="none" stroke="#fff" stroke-width="1.3"/></svg></span>How can the Qur’an be a miracle for the non-Arabs when it is Arabic and they do not<br>know Arabic?.</li>
    <li><span class="bullet"><svg width="7" height="5"><path d="M1 1l2.5 3L6 1" fill="none" stroke="#fff" stroke-width="1.3"/></svg></span>Ruling on offering congratulations at the beginning of the Hijri year.</li>
    <li><span class="bullet"><svg width="7" height="5"><path d="M1 1l2.5 3L6 1" fill="none" stroke="#fff" stroke-width="1.3"/></svg></span>Raising Muslim children in the West to have an aversion to pigs.</li>
    <li><span class="bullet"><svg width="7" height="5"><path d="M1 1l2.5 3L6 1" fill="none" stroke="#fff" stroke-width="1.3"/></svg></span>His mother mistreats his wife and her family.</li>
    <li><span class="bullet"><svg width="7" height="5"><path d="M1 1l2.5 3L6 1" fill="none" stroke="#fff" stroke-width="1.3"/></svg></span>Partner took money from the company without his partner’s knowledge.</li>
    <li><span class="bullet"><svg width="7" height="5"><path d="M1 1l2.5 3L6 1" fill="none" stroke="#fff" stroke-width="1.3"/></svg></span>Ruling on offering congratulations at the beginning of the Hijri year.</li>
    <li><span class="bullet"><svg width="7" height="5"><path d="M1 1l2.5 3L6 1" fill="none" stroke="#fff" stroke-width="1.3"/></svg></span>Raising Muslim children in the West to have an aversion to pigs.</li>
    <li><span class="bullet"><svg width="7" height="5"><path d="M1 1l2.5 3L6 1" fill="none" stroke="#fff" stroke-width="1.3"/></svg></span>His mother mistreats his wife and her family.</li>
    <li><span class="bullet"><svg width="7" height="5"><path d="M1 1l2.5 3L6 1" fill="none" stroke="#fff" stroke-width="1.3"/></svg></span>Partner took money from the company without his partner’s knowledge.</li>
    <li><span class="bullet"><svg width="7" height="5"><path d="M1 1l2.5 3L6 1" fill="none" stroke="#fff" stroke-width="1.3"/></svg></span>Ruling on offering congratulations at the beginning of the Hijri year.</li>
    <li><span class="bullet"><svg width="7" height="5"><path d="M1 1l2.5 3L6 1" fill="none" stroke="#fff" stroke-width="1.3"/></svg></span>Raising Muslim children in the West to have an aversion to pigs.</li>
    <li><span class="bullet"><svg width="7" height="5"><path d="M1 1l2.5 3L6 1" fill="none" stroke="#fff" stroke-width="1.3"/></svg></span>Partner took money from the company without his partner’s knowledge.</li>
  </ul>
</section>

<aside class="abs panel side cats">
  <h2 class="section-title">CATEGORIES</h2>
  <div class="rule"></div>
  <ul class="side-list">
    <li><span class="tick"><svg width="6" height="5"><path d="M.5 2.5l1.8 1.8L5.5.5" fill="none" stroke="#5cb531" stroke-width="1.2"/></svg></span>Basic tenets of faith</li>
    <li><span class="tick"><svg width="6" height="5"><path d="M.5 2.5l1.8 1.8L5.5.5" fill="none" stroke="#5cb531" stroke-width="1.2"/></svg></span>The Quraan and its sciences</li>
    <li><span class="tick"><svg width="6" height="5"><path d="M.5 2.5l1.8 1.8L5.5.5" fill="none" stroke="#5cb531" stroke-width="1.2"/></svg></span>Hadeeth &amp; its Sciences</li>
    <li><span class="tick"><svg width="6" height="5"><path d="M.5 2.5l1.8 1.8L5.5.5" fill="none" stroke="#5cb531" stroke-width="1.2"/></svg></span>Rulings on Jihaad</li>
    <li><span class="tick"><svg width="6" height="5"><path d="M.5 2.5l1.8 1.8L5.5.5" fill="none" stroke="#5cb531" stroke-width="1.2"/></svg></span>Fiqh of the family</li>
    <li style="border:0"><span class="tick"><svg width="6" height="5"><path d="M.5 2.5l1.8 1.8L5.5.5" fill="none" stroke="#5cb531" stroke-width="1.2"/></svg></span>Islamic history and biography</li>
  </ul>
  <a class="full-list" href="#">Full List <span>›</span></a>
</aside>

<aside class="abs panel side files">
  <h2 class="section-title">FILES</h2>
  <div class="rule"></div>
  <ul class="side-list">
    <li><span class="tick"><svg width="6" height="5"><path d="M.5 2.5l1.8 1.8L5.5.5" fill="none" stroke="#5cb531" stroke-width="1.2"/></svg></span>The virtue of fasting ‘Ashoora’</li>
    <li><span class="tick"><svg width="6" height="5"><path d="M.5 2.5l1.8 1.8L5.5.5" fill="none" stroke="#5cb531" stroke-width="1.2"/></svg></span>prohibition on songs and music</li>
    <li><span class="tick"><svg width="6" height="5"><path d="M.5 2.5l1.8 1.8L5.5.5" fill="none" stroke="#5cb531" stroke-width="1.2"/></svg></span>Rulings on witchcraft, the evil eye and destructive envy</li>
    <li><span class="tick"><svg width="6" height="5"><path d="M.5 2.5l1.8 1.8L5.5.5" fill="none" stroke="#5cb531" stroke-width="1.2"/></svg></span>Travel and tourism</li>
    <li><span class="tick"><svg width="6" height="5"><path d="M.5 2.5l1.8 1.8L5.5.5" fill="none" stroke="#5cb531" stroke-width="1.2"/></svg></span>Rulings of wiping over socks</li>
    <li style="border:0"><span class="tick"><svg width="6" height="5"><path d="M.5 2.5l1.8 1.8L5.5.5" fill="none" stroke="#5cb531" stroke-width="1.2"/></svg></span>Rulings of Dreams</li>
  </ul>
  <a class="full-list" href="#">Full List <span>›</span></a>
</aside>

<section class="abs panel topics">
  <div class="abs" style="left:0;top:8px;display:flex">
    <div class="topic"><div class="topic-icon" role="img" aria-label="Counseling illustration" style="background:linear-gradient(#7ec3f2,#2e7fd0)"></div><h3>Counseling</h3><p>Lorem ipsum dolor sit amet,<br>consectetuer adipiscing elit.<br>Praesent vestibulum</p></div>
    <div class="vline"></div>
    <div class="topic"><div class="topic-icon" role="img" aria-label="Acts of worship illustration" style="background:linear-gradient(#fbe08a,#f1a43a)"></div><h3>Jurisprudence of acts of worship</h3><p>Lorem ipsum dolor sit amet,<br>consectetuer adipiscing elit.<br>Praesent vestibulum</p></div>
    <div class="vline"></div>
    <div class="topic"><div class="topic-icon" role="img" aria-label="Muslim minorities illustration" style="background:linear-gradient(#ffd26a,#e8940f)"></div><h3>Jurisprudence of Muslim minorities</h3><p>Lorem ipsum dolor sit amet,<br>consectetuer adipiscing elit.<br>Praesent vestibulum</p></div>
  </div>
  <div class="abs hline"></div>
  <div class="abs" style="left:0;top:136px;display:flex">
    <div class="topic"><div class="topic-icon" role="img" aria-label="Transactions illustration" style="background:linear-gradient(#5a5a5a,#1f1f1f)"></div><h3>Contemporary transactions</h3><p>Lorem ipsum dolor sit amet,<br>consectetuer adipiscing elit.<br>Praesent vestibulum</p></div>
    <div class="vline"></div>
    <div class="topic"><div class="topic-icon" role="img" aria-label="Tenets of faith illustration" style="background:linear-gradient(#e8c98a,#a8742f)"></div><h3>Basic tenets of Faith</h3><p>Lorem ipsum dolor sit amet,<br>consectetuer adipiscing elit.<br>Praesent vestibulum</p></div>
    <div class="vline"></div>
    <div class="topic"><div class="topic-icon" role="img" aria-label="Muslim women illustration" style="background:linear-gradient(#e6e6e6,#9a9a9a)"></div><h3>The Muslim <em>Women</em></h3><p>Lorem ipsum dolor sit amet,<br>consectetuer adipiscing elit.<br>Praesent vestibulum</p></div>
  </div>
</section>

<aside class="abs panel cash-ad">
  <div class="cash-inner">
    <div class="apply" style="top:6px">Apply Now ›</div>
    <div class="cash-head" style="top:36px">Need<br>Fast<br>Cash?</div>
    <div class="cash-mid">
      <ul>
        <li><span class="check"></span>Approval in Seconds</li>
        <li><span class="check"></span>No Credit Check</li>
        <li><span class="check"></span>High Approval Rate</li>
      </ul>
      <strong>Privacy &amp; Security<b>PROTECTED</b></strong>
    </div>
    <div class="cash-head" style="top:238px">Bad<br>Credit<br>OK!</div>
    <div class="apply" style="top:316px">Apply Now ›</div>
  </div>
</aside>

<section class="abs panel finance">
  <div class="finance-inner">
    <div class="finance-text">GLOBAL ISLAMIC FINANCE</div>
    <div class="finance-photo" role="img" aria-label="City skyline with tall towers"></div>
  </div>
</section>

<footer class="abs footer"></footer>
<h2 class="abs about-title">About <span>Tolvene Hub</span></h2>
<p class="abs about-text">Lorem ipsum dolor sit amet, consectetuer adipiscing elit. Pra esent vestibulum molestie lacus. Aenean nonummy hendrerit mauris. Phasellus porta. Fusce suscipit varius mi. Cum sociis natoque penatibus et magnis dis parturient montes, nascetur ridiculus mus.<br><br>Nulla dui. Fusce feugiat malesuada odio. Morbi nunc odio, gravida at, cursus nec, luctus a, lorem.</p>
<div class="abs social" aria-label="Social links">
  <span style="background:#3fa9e6"></span><span style="background:#d9322b"></span><span style="background:#3b5a9a"></span><span style="background:#1a75b1"></span><span style="background:#c9252c"></span>
</div>
<div class="abs foot-col" style="left:363px">
  <h4>COMPANY</h4>
  <ul><li>Home</li><li>About Us</li><li>Contact Us</li><li>NewFatwas</li><li>Privacy Policy</li><li>Articles &amp; Books</li><li>Send A Question</li></ul>
</div>
<div class="abs foot-col" style="left:457px">
  <h4>LANGUAGES</h4>
  <ul><li>中文</li><li>Uygur</li><li>Français</li><li>Español</li><li>日本語</li><li>Indonesian</li><li>Русский new</li><li>Turkish</li></ul>
</div>
<div class="abs foot-col" style="left:550px">
  <h4>DOWNLOAD APPS</h4>
  <div class="store" style="margin-top:8px" role="img" aria-label="App download badge"></div>
  <div class="store" role="img" aria-label="App download badge"></div>
</div>
<div class="abs copyright">© 2013 Website Company Name. All Rights Reserved</div>

</body>
</html>
```